Barristers Chambers - Letterhead and Logo amendments

Brisdane Chambers is a barristers chambers in Marrowby Rise, just around the corner from st. Olvens cathedral. We already have the logo and colour scheme but I think it can be improved, possibly with a better lettermark? we also have a small square version of it.
Main brand colour is: 671E75 – Purple.
Slogan: CONNECTING BARRISTERS, SOLICITORS AND OTHER PROFESSIONALS
I will attach both logos and also our current letterhead, which we made ourselves but it doesn't look professional enough.
Name of the Chambers: Brisdane Chambers
Tagline/Slogan (if any): None
Design Elements:
The logo should be simple and easy to recognize.
It should reflect the nature of the Chambers' work and be relevant to the legal industry.
Any images or graphics used should be unique, professional, and not overly complex.
The logo should be adaptable to various media, such as business cards, letterheads, and digital marketing materials.
It should be legible and easy to read, even when used at a small size.
The colour scheme should be professional and reflect the Chambers' brand identity.
Target Market(s)
Solicitors, lawyers and business clients
Industry/Entity Type
Legal

```html
<!DOCTYPE html>
<html lang="en">
<head>
<meta charset="utf-8">
<title>Brisdane Chambers – Letterhead</title>
<link rel="stylesheet" href="https://fonts.googleapis.com/css2?family=Arimo:wght@400;700&family=Mulish:wght@700&display=swap">
<style>
  :root {
    --brand-purple: #671e75;
    --backdrop: #cbc9ca;
    --paper: #ffffff;
    --ink: #58595b;
    --ink-dark: #4a4a4c;
    --swoosh-grey: #676767;
    --faint: #f2f2f2;
  }
  * { margin: 0; padding: 0; box-sizing: border-box; }
  html, body { width: 1173px; height: 1200px; overflow: hidden; }
  body {
    background: var(--backdrop);
    font-family: "Arimo", Arial, sans-serif;
    color: var(--ink);
    position: relative;
  }
  .letterhead {
    position: absolute;
    left: 230px; top: 96px;
    width: 714px; height: 1009px;
    background: var(--paper);
    box-shadow: 2px 3px 5px rgba(0,0,0,0.25);
    overflow: hidden;
  }
  .brand-name {
    position: absolute; left: 44px; top: 72px;
    font-family: "Arimo", Arial, sans-serif;
    font-size: 27px; font-weight: 400; line-height: 1;
    letter-spacing: 0.5px; text-transform: uppercase;
    color: var(--brand-purple);
    white-space: nowrap;
  }
  .contact {
    position: absolute; left: 492px; top: 48px;
    font-size: 10.6px; line-height: 13px; color: var(--ink);
    font-style: normal;
  }
  .contact .address { margin-bottom: 5px; }
  .contact-row { display: flex; align-items: center; gap: 6px; margin-top: 0.5px; }
  .contact-row svg { width: 8px; height: 8px; fill: var(--brand-purple); flex: none; }
  .header-rule {
    position: absolute; left: 44px; top: 126px;
    width: 624px; height: 1px; background: var(--brand-purple);
  }
  .backdrop-square {
    position: absolute; left: 188px; top: 336px;
    width: 338px; height: 338px;
    border: 12px solid var(--faint);
  }
  .letter {
    position: absolute; left: 64px; top: 311px; width: 586px;
  }
  .salutation {
    font-family: "Mulish", "Century Gothic", sans-serif;
    font-size: 16px; font-weight: 700; color: var(--ink-dark);
    margin-left: 1px; margin-bottom: 28px;
  }
  .body-copy p {
    font-size: 12.3px; line-height: 14.8px;
    margin-bottom: 12.5px; color: var(--ink);
  }
  .signoff {
    font-family: "Mulish", "Century Gothic", sans-serif;
    font-size: 9px; font-weight: 700; color: var(--ink-dark);
    margin-top: 24px; margin-left: 1px;
  }
  .signature {
    margin-top: 30px; width: 117px; height: 35px;
    background: linear-gradient(90deg, #ececec, #f6f6f6);
  }
  .footer-swoosh {
    position: absolute; left: 0; bottom: 0; width: 714px; height: 66px;
  }
</style>
</head>
<body>
  <main class="letterhead">
    <header>
      <div class="brand-name">Brisdane Chambers</div>
      <address class="contact">
        <div class="address">39 Marrowby Rise, Suite 1<br>London EC9X 4QT</div>
        <div class="contact-row">
          <svg viewBox="0 0 10 10" aria-hidden="true"><path d="M2 0.5 L3.6 2.6 L2.8 3.6 Q3.8 5.8 6.3 7.2 L7.4 6.4 L9.5 8 L8.2 9.6 Q4.5 9.2 1.5 5.6 Q0.2 3.6 0.4 1.8 Z"/></svg>
          <span>01632 960418</span>
        </div>
        <div class="contact-row">
          <svg viewBox="0 0 10 10" aria-hidden="true"><path d="M0.5 2 H9.5 V8.2 H0.5 Z M1 2.4 L5 5.6 L9 2.4" stroke="#fff" stroke-width="0.8"/></svg>
          <span>contact@brisdanechambers.co.uk</span>
        </div>
        <div class="contact-row">
          <svg viewBox="0 0 10 10" aria-hidden="true"><circle cx="5" cy="5" r="4.6"/><path d="M2.5 3 Q4 2.5 4.5 4 Q3.5 5.5 5 6.5 M6.5 2 Q7.5 4 6.8 5" stroke="#fff" stroke-width="0.8" fill="none"/></svg>
          <span>www.brisdanechambers.co.uk</span>
        </div>
      </address>
      <div class="header-rule"></div>
    </header>

    <div class="backdrop-square" aria-hidden="true"></div>

    <section class="letter">
      <h1 class="salutation">Dear Mr. Smith,</h1>
      <div class="body-copy">
        <p>Lorem ipsum dolor sit amet, consectetuer adipiscing elit, sed diam nonmmy nibh euismod tincidunt ut laor eet dolore magna aliquam erat volutpat. Ut wisi enim ad minim veniam, quis nostrud exerci tationmcorper suscipit lobortis nisl ut aliquip ex ea commodo consequat. Duis autem vel eum iriure dolor in hendrerit in vulputate velit esse molestie consequat, vel illum dolore eu feugiat</p>
        <p>Rorem ipsum dolor sit amet, consectetuer adipiscing elit, sed diam nonmmy nibh euismod tincidunt ut laor eet dolore magna aliquam erat volutpat. Ut wisi enim ad minim veniam, quis nostrud exerci tationmcorper suscipit lobortis nisl ut aliquip ex ea commodo consequat. Duis autem vel eum iriure dolor in hendrerit in vulputate velit esse molest</p>
        <p>Dorem ipsum dolor sit amet, consectetuer adipiscing elit, sed diam nonmmy nibh euismod tincidunt ut laor eet dolore magna aliquam erat volutpat. Ut wisi enim ad minim veniam, quis nostrud exerci tationmcorper suscipit lobortis nisl ut aliquip ex ea commodo consequat. Duis autem vel eum iriure dolor in hendrerit in suscipit lobortis nisl ut aliquip ex ea commodo consequat. Duis autem vel eum iriure dolor in hendrerit in vulputate velit esse molestie consequat, vel illum</p>
        <p>Sorem ipsum dolor sit amet, consectetuer adipiscing elit, sed diam nonmmy nibh euismod tincidunt ut laor eet dolore magna aliquam erat volutpat. Ut wisi enim ad minim veniam, quis nostrud exerci tationmcorper suscipit lobortis nisl ut aliquip ex ea commodo consequat. Duis autem vel eum iriure dolor in</p>
      </div>
      <p class="signoff">Sincerely,</p>
      <div class="signature" role="img" aria-label="Handwritten signature of the sender"></div>
    </section>

    <svg class="footer-swoosh" viewBox="0 0 714 66" preserveAspectRatio="none" aria-hidden="true">
      <path d="M0 0 Q200 40 481 48 Q200 45 0 19 Z" fill="var(--swoosh-grey)"/>
      <path d="M0 25 Q330 88 714 22 L714 66 L0 66 Z" fill="var(--brand-purple)"/>
    </svg>
  </main>
</body>
</html>
```